Schriftdesign für Shop-Header Bild (Schmuckhandel) / Online-Marketing Material
Zielgruppe
Wir verkaufen Schmuck im Onlineshop mit Herz
Aufgabenstellung
Wir benötigen den vorgegebenen Text in schöner Form, Farbe und Größe harmonisch eingefügt, in unserem Bild.
Folgender Text soll sich schick ins Bild einfügen oder in 3-D vielleicht in Schriftfarbe gold hervorheben:
Mit ganzem Herzen für Sie da!
Ihr Online -Juwelier mit Herz
Siehe auch unser altes Bild mit Text, im Shop, wie es nicht aussehen sollte: www.lindenglanzhof.de

```html
<!DOCTYPE html>
<html lang="de">
<head>
<meta charset="utf-8">
<title>Lindenglanzhof – Ihr Online-Juwelier mit Herz</title>
<link rel="stylesheet" href="https://fonts.googleapis.com/css2?family=Lato:wght@400;700&family=Questrial&family=Handlee&family=Great+Vibes&display=swap">
<style>
  :root {
    --red: #d0101f;
    --red-soft: #e86a72;
    --ink: #222;
    --grey-text: #6b6b6b;
    --nav-bg: #5e5c5e;
    --field-bg: #efefef;
    --white: #fff;
    --dot: #d6d6d6;
  }
  * { box-sizing: border-box; margin: 0; padding: 0; }
  html, body { width: 1200px; height: 855px; overflow: hidden; background: var(--white); }
  body { position: relative; font-family: "Lato", sans-serif; color: var(--ink); }

  .brand { position: absolute; left: 226px; top: 36px; display: flex; align-items: center; gap: 8px; }
  .brand-dot { width: 12px; height: 12px; border-radius: 50%; background: var(--red); }
  .brand-name { font-family: "Lato", sans-serif; font-weight: 700; font-size: 19px; color: var(--red); }

  .top-links { position: absolute; top: 6px; right: 231px; display: flex; gap: 15px; font-size: 9.5px; }
  .top-links a { color: var(--ink); text-decoration: none; }
  .top-links a.is-active { color: var(--red); }

  .search-label { position: absolute; left: 421px; top: 25px; font-size: 12.5px; }
  .search-label::after { content: ""; display: inline-block; margin-left: 7px; border: 4px solid transparent; border-top: 5px solid var(--red); vertical-align: -3px; }
  .search-field { position: absolute; left: 421px; top: 47px; width: 319px; height: 30px; background: var(--field-bg); font-size: 10.5px; color: #888; padding: 9px 18px; }
  .search-field svg { position: absolute; right: 12px; top: 5px; }
  .cart { position: absolute; left: 783px; top: 48px; width: 186px; height: 30px; background: var(--field-bg); font-size: 10.5px; color: var(--red-soft); padding: 9px 18px; }
  .cart svg { position: absolute; right: 16px; top: 5px; }

  .main-nav { position: absolute; left: 0; top: 104px; width: 1200px; height: 33px; background: var(--nav-bg); }
  .main-nav .notch { position: absolute; left: 248px; top: 0; }
  .main-nav ul { list-style: none; position: absolute; left: 324px; top: 9px; display: flex; gap: 29px; font-family: "Questrial", sans-serif; font-size: 12.5px; color: var(--white); letter-spacing: 0.2px; }

  .hero { position: absolute; left: 0; top: 137px; width: 1200px; height: 298px; }
  .hero-photo { position: absolute; inset: 0; background: radial-gradient(ellipse at 60% 45%, #d9b368 0 12%, transparent 22%), linear-gradient(160deg, #e9dfd3 0%, #d7d0c9 35%, #efe8df 60%, #cfc6bd 100%); }
  .hero-line { position: absolute; font-family: "Great Vibes", cursive; color: var(--red); font-size: 34px; text-shadow: 1px 2px 2px rgba(60,0,0,.45); white-space: nowrap; }
  .hero-line--top { left: 238px; top: 163px; }
  .hero-line--bottom { left: 624px; top: 345px; }
  .hero-shade { position: absolute; left: 0; top: 435px; width: 1200px; height: 18px; background: linear-gradient(#e4dcdc, rgba(255,255,255,0)); }

  .seal { position: absolute; left: 740px; top: 462px; width: 106px; height: 64px; }

  .dotted { position: absolute; left: 727px; width: 243px; height: 4px; background: radial-gradient(circle, var(--dot) 1.6px, transparent 2px) 0 0 / 8.5px 4px repeat-x; }
  .benefits { position: absolute; left: 730px; top: 558px; list-style: none; font-size: 12.5px; color: var(--red); }
  .benefits li { display: flex; align-items: center; gap: 8px; height: 30px; }

  .store-note { position: absolute; left: 230px; top: 535px; font-size: 14px; color: var(--grey-text); }
  .store-note a { font-size: 12px; color: var(--grey-text); text-decoration: none; }
  .store-banner { position: absolute; left: 230px; top: 569px; width: 466px; height: 156px; background: linear-gradient(90deg, #262626 0%, #3b3b3b 45%, #7a4a24 70%, #e48a2a 78%, #4a4a4a 100%); box-shadow: 0 1px 3px rgba(0,0,0,.35); }
  .store-name { position: absolute; left: 12px; top: 12px; font-family: "Lato", sans-serif; font-size: 30px; color: #c9a552; letter-spacing: 1px; }
  .store-dots { position: absolute; right: 22px; bottom: 12px; display: flex; gap: 7px; }
  .store-dots span { width: 8px; height: 8px; border-radius: 50%; background: var(--white); }
  .store-dots span.is-current { background: var(--red); }

  .welcome { position: absolute; left: 230px; top: 771px; font-family: "Handlee", cursive; font-size: 20px; color: var(--grey-text); }
  .welcome em { font-style: normal; color: var(--red); }
  .tagline { position: absolute; left: 230px; top: 817px; font-size: 15px; font-weight: 700; color: var(--grey-text); }
</style>
</head>
<body>
  <header>
    <div class="brand"><span class="brand-dot"></span><span class="brand-name">Lindenglanzhof</span></div>
    <nav class="top-links">
      <a class="is-active" href="#">Startseite</a><a href="#">Anmelden</a><a href="#">Mein Konto</a><a href="#">Newsletter abonnieren</a><a href="#">Kontakt</a>
    </nav>
    <div class="search-label">Nach welchem Artikel suchen Sie?</div>
    <div class="search-field">Suchen nach
      <svg width="22" height="20" viewBox="0 0 22 20"><path d="M11 19 C4 13 1 10 1 6 A5 5 0 0 1 11 4 A5 5 0 0 1 21 6 C21 10 18 13 11 19Z" fill="var(--red)"/><circle cx="10.5" cy="8.5" r="2.5" fill="none" stroke="#fff" stroke-width="1.4"/><line x1="12.3" y1="10.3" x2="14" y2="12" stroke="#fff" stroke-width="1.4"/></svg>
    </div>
    <div class="cart">Ihr Warenkorb ist leer.
      <svg width="16" height="19" viewBox="0 0 16 19"><rect x="0" y="5" width="16" height="14" rx="1" fill="var(--red)"/><path d="M5 6 V3 A3 3 0 0 1 11 3 V6" fill="none" stroke="var(--red)" stroke-width="1.5"/><path d="M8 15 C5 13 4 12 4 10.5 A2 2 0 0 1 8 10 A2 2 0 0 1 12 10.5 C12 12 11 13 8 15Z" fill="#fff"/></svg>
    </div>
  </header>

  <nav class="main-nav">
    <svg class="notch" width="62" height="23" viewBox="0 0 62 23"><path d="M0 0 L62 0 L31 23 Z" fill="var(--white)"/></svg>
    <ul><li>KREUZ-ANHÄNGER</li><li>ANHÄNGER/VERSCH.</li><li>FOTO-MEDAILLONS</li><li>OHRSCHMUCK</li><li>ACCESSOIRES</li></ul>
  </nav>

  <section class="hero">
    <div class="hero-photo" role="img" aria-label="Goldener Herzanhänger an feiner Kette auf cremefarbenem Seidenstoff"></div>
  </section>
  <div class="hero-line hero-line--top">Mit ganzem Herzen für Sie da!</div>
  <div class="hero-line hero-line--bottom">Ihr Online -Juwelier mit Herz</div>
  <div class="hero-shade"></div>

  <svg class="seal" viewBox="0 0 106 64" role="img" aria-label="Gütesiegel">
    <rect x="40" y="18" width="64" height="26" rx="3" fill="#e2c15e"/>
    <circle cx="32" cy="32" r="31" fill="#25306e"/>
    <circle cx="32" cy="32" r="17" fill="#d7aa3a"/>
  </svg>

  <div class="dotted" style="top:534px"></div>
  <ul class="benefits">
    <li><svg width="24" height="22" viewBox="0 0 24 22"><path d="M12 21 C4 15 1 11 1 7 A5.5 5.5 0 0 1 12 4.5 A5.5 5.5 0 0 1 23 7 C23 11 20 15 12 21Z" fill="#f6c6ca" stroke="var(--red-soft)" stroke-width="1.3"/></svg>Versand innerhalb von 24 Stunden</li>
    <li><svg width="24" height="22" viewBox="0 0 24 22"><path d="M12 21 C4 15 1 11 1 7 A5.5 5.5 0 0 1 12 4.5 A5.5 5.5 0 0 1 23 7 C23 11 20 15 12 21Z" fill="#f6c6ca" stroke="var(--red-soft)" stroke-width="1.3"/></svg>schneller, persönlicher Service</li>
    <li><svg width="24" height="22" viewBox="0 0 24 22"><path d="M12 21 C4 15 1 11 1 7 A5.5 5.5 0 0 1 12 4.5 A5.5 5.5 0 0 1 23 7 C23 11 20 15 12 21Z" fill="#f6c6ca" stroke="var(--red-soft)" stroke-width="1.3"/></svg>Kundenzufriedenheit an erster Stelle</li>
    <li><svg width="24" height="22" viewBox="0 0 24 22"><path d="M12 21 C4 15 1 11 1 7 A5.5 5.5 0 0 1 12 4.5 A5.5 5.5 0 0 1 23 7 C23 11 20 15 12 21Z" fill="#f6c6ca" stroke="var(--red-soft)" stroke-width="1.3"/></svg>sichere Zahlungsmethoden</li>
  </ul>
  <div class="dotted" style="top:685px"></div>

  <p class="store-note">Besuchen Sie auch unseren VELTARIS-Schmuck Store: <a href="#">hier</a></p>
  <div class="store-banner" role="img" aria-label="Werbebanner: Schmuckherstellung mit Flamme und Zange, Hinweis auf Fertigung in Deutschland">
    <span class="store-name">VELTARIS</span>
    <div class="store-dots"><span></span><span></span><span class="is-current"></span><span></span><span></span><span></span></div>
  </div>

  <h1 class="welcome">Herzlich Willkommen im <em>Lindenglanzhof.de</em> Schmuck-Shop</h1>
  <h2 class="tagline">Ihr Online-Juwelier mit Herz</h2>
</body>
</html>
```